High end personal training flyer design

I want a flyer designed to be delivered to people's houses to interest them in high end (and, therefore, not cheap) personal training services.

Don't want standard pictures of people exercising, before and afters, etc. More something that will appeal to that more affluent market.

Flexible on size of flyer, but please make sure it is a standard size that I can get printed easily. Would like it not to look like a normal flyer you get through the letterbox, so if any particular sizes, shapes, etc are known to do that, then that would be a good start.

Text on flyer to be as follows:

Is this you:

Live in East Cheshire
Male, aged 30-50
A father
Cash rich, time poor
Find handling high pressure at work comfortable
But have a short fuse out of work – with the wife, kids, life in general, etc
Not happy with the way your body looks and feels
Know exactly what you should do to sort that, but struggling to actually do it for various reasons
Turned off by the standard menu of options for addressing that – gyms, slimming clubs, diets, etc

If so, you may be interested in what I do.

Some would call it Personal Training. Some would call it Coaching. I’m not interested in giving what I do labels.

What I am interested in is providing the best possible service (and results) for my clients – whatever that entails.

I work closely with one or two clients at a time to make sure they get exactly what they need.

If you would like to find out more about this, I usually meet for a coffee and a chat. To see if we both think our working together is a good idea.

No squeeze pages, no countdowns, mailing lists or false scarcity.

No plastering this flyer with ‘Before and afters’ – they are ten a penny and my clients don’t want to have pictures of them in their underwear spread around the local area.

Just give me a call and we’ll go from there.

My number is 07912645320.

Tim

Industry/Entity Type

Training

Requirements
Should not have
• Generic before and after or exercise type pictures

```html
<!DOCTYPE html>
<html lang="en">
<head>
<meta charset="utf-8">
<title>Personal Training Flyer – Tim</title>
<link rel="stylesheet" href="https://fonts.googleapis.com/css2?family=Raleway:ital,wght@0,400;0,600;0,700;1,400&family=Oswald:wght@700&display=swap">
<style>
  :root {
    --page-bg: #ecebe8;
    --paper: #ffffff;
    --ink: #1f1f1f;
    --night: #000000;
    --signal-red: #e31b23;
    --white: #ffffff;
    --photo-light: #4a3a30;
    --photo-dark: #070707;
  }
  * { box-sizing: border-box; margin: 0; padding: 0; }
  html, body { width: 900px; height: 1200px; overflow: hidden; }
  body { background: var(--page-bg); font-family: "Raleway", Arial, sans-serif; position: relative; }

  .flyer {
    position: absolute; left: 82px; top: 72px;
    width: 736px; height: 1046px;
    background: var(--paper); overflow: hidden;
  }
  .flyer-art { position: absolute; inset: 0; width: 736px; height: 1046px; }

  .headline {
    position: absolute; right: 60px; top: 462px;
    font-family: "Oswald", "Arial Narrow", sans-serif; font-weight: 700;
    font-size: 40px; line-height: 52px; color: var(--white); letter-spacing: 0.2px;
  }

  .intro {
    position: absolute; left: 25px; top: 574px; width: 328px;
    color: var(--ink); font-size: 16px; line-height: 20px;
  }
  .intro p { margin-bottom: 10px; }
  .intro strong { font-weight: 700; }

  .checklist {
    position: absolute; left: 381px; top: 550px; width: 340px;
    list-style: none; color: var(--white); font-size: 16px; line-height: 20px;
  }
  .checklist li { position: relative; padding-left: 22px; margin-bottom: 5px; }
  .checklist .tick { position: absolute; left: 0; top: 2px; width: 17px; height: 17px; }

  .cta { position: absolute; left: 381px; top: 944px; width: 340px; }
  .cta-lead { color: var(--white); font-weight: 700; font-size: 16px; line-height: 20px; }
  .cta-call { color: var(--signal-red); font-size: 13px; line-height: 18px; text-transform: uppercase; margin-top: 6px; }
  .cta-phone { display: flex; align-items: center; margin-top: 8px; margin-left: 21px; color: var(--white); }
  .cta-phone svg { width: 31px; height: 31px; margin-right: 8px; }
  .cta-phone .number { font-weight: 700; font-size: 27px; letter-spacing: 0.3px; }
  .cta-phone .name { font-style: italic; font-size: 27px; margin-left: 8px; }
</style>
</head>
<body>
  <main class="flyer">
    <svg class="flyer-art" viewBox="0 0 736 1046">
      <defs>
        <radialGradient id="photo-tone" cx="0.5" cy="0.55" r="0.55">
          <stop offset="0" stop-color="var(--photo-light)"/>
          <stop offset="1" stop-color="var(--photo-dark)"/>
        </radialGradient>
      </defs>
      <!-- right-hand dark panel -->
      <rect class="dark-panel" x="368" y="0" width="368" height="1046" fill="var(--night)"/>
      <!-- red brush band -->
      <polygon class="red-band" points="470,0 736,0 736,205 555,325 520,270 560,150" fill="var(--signal-red)"/>
      <g class="band-streaks" stroke="var(--white)" stroke-width="3" stroke-linecap="round">
        <line x1="520" y1="170" x2="736" y2="70"/>
        <line x1="545" y1="215" x2="736" y2="130"/>
        <line x1="560" y1="250" x2="690" y2="195"/>
      </g>
      <polygon class="corner-accent" points="0,0 60,0 0,40" fill="var(--signal-red)"/>
      <polygon class="corner-accent" points="0,466 22,476 0,484" fill="var(--signal-red)"/>
      <!-- photo frame -->
      <circle class="photo-ring" cx="248" cy="263" r="268" fill="var(--white)"/>
      <circle class="photo" cx="248" cy="263" r="255" fill="url(#photo-tone)" role="img" aria-label="Photograph of a muscular man posing with arms spread against a dark background"/>
      <!-- headline brush bar -->
      <polygon class="headline-bar" points="358,470 708,452 704,520 346,540" fill="var(--signal-red)"/>
    </svg>

    <h1 class="headline">IS THIS YOU:</h1>

    <section class="intro">
      <p>Some would call it <strong>Personal Training.</strong> Some would call it Coaching. I’m not interested in giving what I do labels.</p>
      <p>What I am interested in is providing the best possible service (and results) for my clients – whatever that entails.</p>
      <p>I work closely with one or two clients at a time to make sure they get exactly what they need.</p>
      <p>If you would like to find out more about this, I usually meet for a coffee and a chat. To see if we both think our working together is a good idea.</p>
      <p>No squeeze pages, no countdowns, mail-ing lists or false scarcity.</p>
      <p>No plastering this flyer with ‘Before and afters’ – they are ten a penny and my clients don’t want to have pictures of them in their underwear spread around the local area.</p>
    </section>

    <ul class="checklist">
      <li><svg class="tick" viewBox="0 0 20 20"><circle cx="10" cy="10" r="9" fill="var(--signal-red)"/><path d="M5.5 10.3l3 3 6-6.3" fill="none" stroke="var(--white)" stroke-width="2.2"/></svg>Live in East Cheshire</li>
      <li><svg class="tick" viewBox="0 0 20 20"><circle cx="10" cy="10" r="9" fill="var(--signal-red)"/><path d="M5.5 10.3l3 3 6-6.3" fill="none" stroke="var(--white)" stroke-width="2.2"/></svg>Male, aged 30-50</li>
      <li><svg class="tick" viewBox="0 0 20 20"><circle cx="10" cy="10" r="9" fill="var(--signal-red)"/><path d="M5.5 10.3l3 3 6-6.3" fill="none" stroke="var(--white)" stroke-width="2.2"/></svg>A father</li>
      <li><svg class="tick" viewBox="0 0 20 20"><circle cx="10" cy="10" r="9" fill="var(--signal-red)"/><path d="M5.5 10.3l3 3 6-6.3" fill="none" stroke="var(--white)" stroke-width="2.2"/></svg>Cash rich, time poor</li>
      <li><svg class="tick" viewBox="0 0 20 20"><circle cx="10" cy="10" r="9" fill="var(--signal-red)"/><path d="M5.5 10.3l3 3 6-6.3" fill="none" stroke="var(--white)" stroke-width="2.2"/></svg>Find handling high pressure at work comfortable</li>
      <li><svg class="tick" viewBox="0 0 20 20"><circle cx="10" cy="10" r="9" fill="var(--signal-red)"/><path d="M5.5 10.3l3 3 6-6.3" fill="none" stroke="var(--white)" stroke-width="2.2"/></svg>But have a short fuse out of work – with the wife, kids, life in general, etc</li>
      <li><svg class="tick" viewBox="0 0 20 20"><circle cx="10" cy="10" r="9" fill="var(--signal-red)"/><path d="M5.5 10.3l3 3 6-6.3" fill="none" stroke="var(--white)" stroke-width="2.2"/></svg>Not happy with the way your body looks and feels</li>
      <li><svg class="tick" viewBox="0 0 20 20"><circle cx="10" cy="10" r="9" fill="var(--signal-red)"/><path d="M5.5 10.3l3 3 6-6.3" fill="none" stroke="var(--white)" stroke-width="2.2"/></svg>Know exactly what you should do to sort that, but struggling to actually do it for various reasons</li>
      <li><svg class="tick" viewBox="0 0 20 20"><circle cx="10" cy="10" r="9" fill="var(--signal-red)"/><path d="M5.5 10.3l3 3 6-6.3" fill="none" stroke="var(--white)" stroke-width="2.2"/></svg>Turned off by the standard menu of options for addressing that – gyms, slimming clubs, diets, etc</li>
    </ul>

    <section class="cta">
      <p class="cta-lead">If so, you may be interested in what I do.</p>
      <p class="cta-call">Just give me a call and we’ll go from there.</p>
      <p class="cta-phone">
        <svg viewBox="0 0 32 32"><circle cx="16" cy="16" r="15" fill="var(--signal-red)"/><path d="M11.2 8.5l2.6-.6 1.6 4-1.8 1.4c.9 2 2.4 3.6 4.4 4.6l1.5-1.8 4 1.6-.6 2.6c-.3 1-1.2 1.6-2.2 1.5C14.4 21.2 10.3 17 9.7 10.7c-.1-1 .5-1.9 1.5-2.2z" fill="var(--white)"/></svg>
        <span class="number">07912645320</span><span class="name">- Tim</span>
      </p>
    </section>
  </main>
</body>
</html>
```